Ferris Contracting LLC Business Card Design

I am looking for a creative and unique business card design. We are a commercial construction general contractor. With the name "FERRIS" Contracting, I am hoping to see some neat designs that correlate with the name.

```html
<!DOCTYPE html>
<html lang="en">
<head>
<meta charset="utf-8">
<title>Ferris Contracting LLC – Business Card</title>
<link href="https://fonts.googleapis.com/css2?family=Inter:wght@400;500;700;800&display=swap" rel="stylesheet">
<style>
  :root {
    --backdrop: #e9e7e4;
    --card-dark: #1d1e20;
    --card-light: #ffffff;
    --brand-blue: #0a8ad6;
    --ink: #2e2f31;
    --ink-soft: #67686b;
    --rule: #4a4b4e;
  }
  * { margin: 0; padding: 0; box-sizing: border-box; }
  html, body {
    width: 1200px; height: 1200px; overflow: hidden;
    background: var(--backdrop);
    font-family: "Inter", Arial, sans-serif;
  }
  .canvas { position: relative; width: 1200px; height: 1200px; }
  .card {
    position: absolute; left: 179px; width: 861px; height: 495px;
    box-shadow: 0 6px 18px rgba(0,0,0,.18);
  }
  .card--front { top: 84px; background: var(--card-dark); }
  .card--back { top: 622px; background: var(--card-light); }

  .brand-mark {
    position: absolute; display: flex; align-items: center;
    color: var(--brand-blue); font-weight: 800; text-transform: uppercase;
    white-space: nowrap;
  }
  .brand-mark__dot { flex: none; border-radius: 50%; background: var(--brand-blue); }
  .brand-mark__name { display: flex; flex-direction: column; line-height: 1; }

  .card--front .brand-mark {
    left: 0; right: 0; top: 160px; justify-content: center; gap: 34px;
    font-size: 66px; letter-spacing: 3px;
  }
  .card--front .brand-mark__dot { width: 150px; height: 150px; }
  .card--front .brand-mark__name { gap: 14px; }

  .card--back .brand-mark {
    right: 46px; top: 62px; gap: 18px;
    font-size: 36px; letter-spacing: 2px;
  }
  .card--back .brand-mark__dot { width: 82px; height: 82px; }
  .card--back .brand-mark__name { gap: 8px; }

  .person { position: absolute; left: 33px; top: 268px; }
  .person__name { font-size: 36px; font-weight: 700; color: var(--ink); line-height: 1.05; letter-spacing: 0.5px; }
  .person__role { font-size: 27px; font-weight: 500; color: var(--ink-soft); letter-spacing: 3px; line-height: 1.1; }

  .divider {
    position: absolute; left: 33px; top: 344px; width: 793px; height: 2px;
    background: linear-gradient(to right, var(--brand-blue) 0 128px, var(--rule) 128px);
  }

  .contact { position: absolute; left: 33px; top: 355px; list-style: none; }
  .contact__item {
    display: flex; align-items: center; gap: 14px; height: 38px;
    font-size: 25px; font-weight: 500; color: var(--ink-soft); letter-spacing: 4.5px;
  }
  .contact__item--phone { letter-spacing: 4px; }
  .contact__icon { width: 26px; height: 26px; flex: none; }
</style>
</head>
<body>
<main class="canvas">
  <section class="card card--front" aria-label="Card front">
    <div class="brand-mark">
      <span class="brand-mark__dot"></span>
      <span class="brand-mark__name"><span>Ferris</span><span>Contracting</span></span>
    </div>
  </section>

  <section class="card card--back" aria-label="Card back">
    <div class="brand-mark">
      <span class="brand-mark__dot"></span>
      <span class="brand-mark__name"><span>Ferris</span><span>Contracting</span></span>
    </div>

    <div class="person">
      <p class="person__name">Name Surename</p>
      <p class="person__role">Director</p>
    </div>

    <div class="divider"></div>

    <ul class="contact">
      <li class="contact__item contact__item--phone">
        <svg class="contact__icon" viewBox="0 0 24 24" fill="#2e2f31" aria-hidden="true">
          <path d="M6.6 10.8a15.2 15.2 0 0 0 6.6 6.6l2.2-2.2a1 1 0 0 1 1-.25 11.4 11.4 0 0 0 3.6.57 1 1 0 0 1 1 1V20a1 1 0 0 1-1 1A17 17 0 0 1 3 4a1 1 0 0 1 1-1h3.5a1 1 0 0 1 1 1c0 1.25.2 2.46.57 3.6a1 1 0 0 1-.25 1z"/>
          <path d="M14 3.5a7 7 0 0 1 6.5 6.5M14 6.8a3.8 3.8 0 0 1 3.2 3.2" fill="none" stroke="#2e2f31" stroke-width="1.8" stroke-linecap="round"/>
        </svg>
        <span>0412 555 019</span>
      </li>
      <li class="contact__item">
        <svg class="contact__icon" viewBox="0 0 24 24" aria-hidden="true">
          <rect x="2" y="6" width="20" height="13" fill="#2e2f31"/>
          <path d="M2.5 6.5 12 13.5l9.5-7M2.5 18.5l7-6M21.5 18.5l-7-6" fill="none" stroke="#fff" stroke-width="1.4"/>
        </svg>
        <span>email@website.com</span>
      </li>
      <li class="contact__item">
        <svg class="contact__icon" viewBox="0 0 24 24" fill="none" stroke="#2e2f31" stroke-width="1.8" aria-hidden="true">
          <circle cx="12" cy="12" r="9.5"/>
          <ellipse cx="12" cy="12" rx="4" ry="9.5"/>
          <path d="M2.5 12h19M4 7h16M4 17h16"/>
        </svg>
        <span>www.website.com</span>
      </li>
    </ul>
  </section>
</main>
</body>
</html>
```